Marrowfield Light Brown Inventory Reduction Sale

- We are having an inventory reduction sale on our 18g Marrowfield Light Brown Casket.
- Original price $954, Sale price $799, savings of $155. Sale
will be March 23 - 27.
- Orders must be placed online at Hadley-Corvane.com. Casket details - This 18g steel gasketed casket features a Light Brown exterior with a RoseSand velvet interior. This casket features an oversized interior - 27.5" x 82.5".
- We will need the following disclaimer listed - This offer is valid only while supplies last. Discount prices are not available with any other offers or discounts. Due to limitations of computer screens and color printers, the color of the product may vary from the photographs. )

- (Included is a copy of an ad that we had previously designed)

```html
<!DOCTYPE html>
<html lang="en">
<head>
<meta charset="utf-8">
<title>Marrowfield Light Brown – Inventory Reduction Sale</title>
<link rel="stylesheet" href="https://fonts.googleapis.com/css2?family=Cinzel:wght@400;700&family=Playball&family=Source+Sans+3:wght@400;600&display=swap">
<style>
  :root {
    --page-bg: #e4e2df;
    --paper-top: #f6f6f6;
    --paper-mid: #ebeaea;
    --sand-light: #d4c8c0;
    --sand: #c5b6ad;
    --sand-panel: #d6cbc3;
    --ink: #4f423d;
    --ink-soft: #8a766b;
    --script: #a88f82;
    --pill: #8e7b71;
    --fine-print: #a8968d;
    --white: #ffffff;
  }
  * { box-sizing: border-box; margin: 0; padding: 0; }
  html, body { width: 1078px; height: 1200px; overflow: hidden; background: var(--page-bg); }
  .flyer {
    position: absolute; left: 91px; top: 21px; width: 896px; height: 1158px;
    background: linear-gradient(180deg, var(--paper-top), var(--paper-mid));
    overflow: hidden;
  }
  .backdrop { position: absolute; inset: 0; width: 100%; height: 100%; }
  .headline {
    position: absolute; left: 48px; right: 38px; top: 20px; height: 69px;
    border-top: 2px solid var(--ink-soft); border-bottom: 2px solid var(--ink-soft);
    display: flex; align-items: center; justify-content: center;
    font-family: "Cinzel", serif; font-weight: 400; font-size: 40px; color: var(--ink-soft); letter-spacing: 1px;
  }
  .headline strong { color: var(--ink); font-weight: 700; margin-left: 12px; }
  .product-photo {
    position: absolute; left: 102px; top: 133px; width: 716px; height: 410px;
    background: radial-gradient(ellipse at 45% 45%, #f4efe9 0%, #e2cfc3 40%, #cfae9c 62%, rgba(207,174,156,0) 72%);
  }
  .product-name {
    position: absolute; right: 40px; top: 575px; text-align: right;
    font-family: "Playball", cursive; font-weight: 400; font-size: 46px; line-height: 50px; color: var(--script);
  }
  .details { position: absolute; left: 37px; top: 735px; width: 400px; }
  .details-kicker { font-family: "Playball", cursive; font-size: 40px; line-height: 40px; color: var(--ink-soft); }
  .details-title { font-family: "Cinzel", serif; font-weight: 400; font-size: 54px; line-height: 56px; color: var(--ink-soft); letter-spacing: 2px; }
  .details-copy {
    margin-top: 14px; width: 380px; font-family: "Source Sans 3", sans-serif; font-size: 16.5px; line-height: 24px; color: var(--white);
  }
  .brand-name {
    position: absolute; left: 37px; top: 982px;
    font-family: "Source Sans 3", sans-serif; font-weight: 600; font-size: 24px; color: var(--white); letter-spacing: 1px;
  }
  .pricing { position: absolute; right: 40px; top: 755px; text-align: right; font-family: "Cinzel", serif; color: var(--ink); }
  .pricing-label { font-size: 48px; font-weight: 700; letter-spacing: 4px; line-height: 54px; }
  .pricing-now { font-size: 118px; line-height: 120px; }
  .pricing-was { font-size: 32px; line-height: 40px; margin-top: 6px; }
  .pricing-was .old { position: relative; display: inline-block; margin-right: 12px; }
  .pricing-was .old svg { position: absolute; left: 0; top: 0; width: 100%; height: 100%; }
  .pricing-dates { margin-top: 6px; font-size: 22px; line-height: 28px; letter-spacing: 2px; color: var(--ink-soft); }
  .order-bar {
    position: absolute; left: 124px; top: 1045px; width: 653px; height: 44px; border-radius: 22px;
    background: var(--pill); color: var(--white);
    display: flex; align-items: center; justify-content: center; gap: 10px;
    font-family: "Source Sans 3", sans-serif; font-size: 23px;
  }
  .order-bar strong { font-weight: 600; }
  .order-bar svg { width: 20px; height: 20px; }
  .fine-print {
    position: absolute; left: 38px; right: 38px; top: 1106px; text-align: center;
    font-family: "Source Sans 3", sans-serif; font-size: 11px; line-height: 15px; color: var(--fine-print);
  }
</style>
</head>
<body>
<main class="flyer">
  <svg class="backdrop" viewBox="0 0 613 792" preserveAspectRatio="none" aria-hidden="true">
    <path d="M0,392 C150,470 380,440 613,318 L613,792 L0,792 Z" fill="var(--sand-light)"/>
    <path d="M0,392 C180,480 420,500 613,488 L613,792 L0,792 Z" fill="var(--sand)"/>
    <path d="M268,792 C268,640 330,520 613,470 L613,792 Z" fill="var(--sand-panel)"/>
  </svg>

  <h1 class="headline">INVENTORY REDUCTION <strong>SALE!</strong></h1>

  <div class="product-photo" role="img" aria-label="Photo of the Marrowfield Light Brown steel casket, lid open, with a pale velvet interior"></div>

  <h2 class="product-name">Marrowfield<br>Light Brown</h2>

  <section class="details">
    <div class="details-kicker">Casket</div>
    <h3 class="details-title">DETAILS</h3>
    <p class="details-copy">This 18g steel gasketed casket features a Light Brown exterior with a RoseSand velvet interior.&nbsp; This casket features an oversized interior - 27.5" x 82.5".</p>
  </section>

  <div class="brand-name">HADLEY CORVANE</div>

  <section class="pricing">
    <div class="pricing-label">SALE</div>
    <div class="pricing-now">$799</div>
    <div class="pricing-was">
      <span class="old">$954<svg viewBox="0 0 100 40" preserveAspectRatio="none" aria-hidden="true"><path d="M40,2 L96,38 M96,2 L40,38" stroke="var(--ink-soft)" stroke-width="2" fill="none"/></svg></span>SAVE $155
    </div>
    <div class="pricing-dates">MARCH 23 – 27</div>
  </section>

  <div class="order-bar">
    Orders must be placed online at
    <svg viewBox="0 0 20 20" aria-hidden="true"><circle cx="10" cy="10" r="8" fill="none" stroke="#fff" stroke-width="1.6"/><ellipse cx="10" cy="10" rx="3.5" ry="8" fill="none" stroke="#fff" stroke-width="1.4"/><path d="M2,10 H18" stroke="#fff" stroke-width="1.4"/></svg>
    <strong>Hadley-Corvane.com</strong>
  </div>

  <p class="fine-print">This offer is valid only while supplies last. Discount prices are not available with any other offers or discounts. Due to limitations of computer screens<br>and color printers, the color of the product may vary from the photographs.</p>
</main>
</body>
</html>
```